Business Card & Email Signature Design || Upmarket + Luxury

Riverlume Honey, a New Zealand Manuka Honey company needs a Business Card & Email Signature design.

Our logo's are attached in Gold & Black versions, feel free to be creative with how you use the logo and it's patterns in your design.

Style:
- Looking for an Elegant, Luxurious, Upmarket feel.
- Black/Matte Black Card, Gold Foil, UV Embossing

Information to Add:

- Logo
- Company Name: Riverlume Honey
- Name: Mattias Brovell
- Title: Creative Director
- Phone: +64 2919 58 617
- Email: mattias@riverlumehoney.example
- Website: www.riverlumehoney.example

- Socials: ***For email Signature Only***
- Facebook: https://www.facebook.com/riverlumehoney/
- Instagram: https://www.instagram.com/riverlumehoney/

Target Market(s)

Asia/Europe Luxury, Upmarket

Contact Information for Business Card

- Logo
- Name: Mattias Brovell
- Phone: +64 2919 58 617

Font styles to use
Other font styles liked:
• Champagne & Limousines (Attached)

Requirements
Must have
• Business Card & Email Signature Design.

Looking for a Sleek, Luxury, Upmarket Design.

```html
<!DOCTYPE html>
<html lang="en">
<head>
<meta charset="UTF-8">
<title>Riverlume Honey — Business Card</title>
<link href="https://fonts.googleapis.com/css2?family=Montserrat:wght@300;400;700&display=swap" rel="stylesheet">
<style>
  :root {
    --backdrop: #1b1b1c;
    --card: #121212;
    --gold: #c9a24a;
    --gold-light: #f0d27a;
    --gold-deep: #8a6420;
  }
  * { margin: 0; padding: 0; box-sizing: border-box; }
  html, body {
    width: 1200px; height: 900px; overflow: hidden;
    background: var(--backdrop);
    font-family: "Montserrat", sans-serif;
    color: var(--gold);
  }
  .canvas { position: relative; width: 1200px; height: 900px; }
  .card {
    position: absolute; left: 280px; width: 640px; height: 366px;
    background: var(--card);
    overflow: hidden;
  }
  .card-front { top: 60px; }
  .card-back { top: 474px; }
  .gold-edge {
    position: absolute; left: 0; right: 0; bottom: 0; height: 5px;
    background: linear-gradient(90deg, var(--gold-deep), var(--gold-light) 45%, var(--gold) 60%, var(--gold-deep));
  }

  /* Front */
  .front-mark {
    position: absolute; left: 0; right: 0; top: 104px;
    display: flex; flex-direction: column; align-items: center; gap: 22px;
  }
  .mark-circle {
    width: 58px; height: 58px; border-radius: 50%;
    border: 2px solid var(--gold);
  }
  .front-name {
    font-weight: 300; font-size: 24px; letter-spacing: 6px;
    text-transform: uppercase;
  }

  /* Back */
  .brand-block {
    position: absolute; left: 40px; top: 118px; width: 220px;
    display: flex; flex-direction: column; align-items: center; gap: 16px;
  }
  .brand-circle {
    width: 44px; height: 44px; border-radius: 50%;
    border: 2px solid var(--gold);
  }
  .brand-name {
    font-weight: 300; font-size: 19px; letter-spacing: 3px;
    text-transform: uppercase; text-align: center; line-height: 1.25;
  }
  .divider {
    position: absolute; left: 282px; top: 100px;
    width: 2px; height: 150px; background: var(--gold);
  }
  .contact-block { position: absolute; left: 310px; top: 110px; }
  .person-name {
    font-weight: 700; font-size: 25px; letter-spacing: 1.5px;
    text-transform: uppercase; line-height: 1;
  }
  .person-title { font-weight: 400; font-size: 16px; margin-top: 6px; letter-spacing: 0.5px; }
  .contact-list { list-style: none; margin-top: 22px; }
  .contact-list li {
    display: flex; align-items: center; gap: 8px;
    font-weight: 400; font-size: 15px; line-height: 1.55;
  }
  .contact-list svg { width: 13px; height: 13px; flex: none; }
</style>
</head>
<body>
<div class="canvas">

  <section class="card card-front">
    <div class="front-mark">
      <div class="mark-circle"></div>
      <div class="front-name">Riverlume Honey Co.</div>
    </div>
    <div class="gold-edge"></div>
  </section>

  <section class="card card-back">
    <div class="brand-block">
      <div class="brand-circle"></div>
      <div class="brand-name">Riverlume Honey</div>
    </div>

    <div class="divider"></div>

    <div class="contact-block">
      <div class="person-name">Mattias Brovell</div>
      <div class="person-title">Creative Director</div>
      <ul class="contact-list">
        <li>
          <svg viewBox="0 0 16 16" aria-hidden="true"><path d="M4 1.5 6 4.5 4.6 6.2c.9 2 2.3 3.4 4.2 4.3L10.5 9l3 2-1.2 2.6c-5.5-.2-10-4.7-10.3-10.2Z" fill="none" stroke="currentColor" stroke-width="1.4" stroke-linejoin="round"/></svg>
          +64 2919 58 617
        </li>
        <li>
          <svg viewBox="0 0 16 16" aria-hidden="true"><rect x="1.5" y="3.5" width="13" height="9" fill="none" stroke="currentColor" stroke-width="1.4"/><path d="M1.5 3.8 8 9l6.5-5.2" fill="none" stroke="currentColor" stroke-width="1.4"/></svg>
          mattias@riverlumehoney.example
        </li>
        <li>
          <svg viewBox="0 0 16 16" aria-hidden="true"><circle cx="8" cy="8" r="6.3" fill="none" stroke="currentColor" stroke-width="1.3"/><ellipse cx="8" cy="8" rx="2.8" ry="6.3" fill="none" stroke="currentColor" stroke-width="1.1"/><path d="M1.7 8h12.6" stroke="currentColor" stroke-width="1.1"/></svg>
          www.riverlumehoney.example
        </li>
      </ul>
    </div>

    <div class="gold-edge"></div>
  </section>

</div>
</body>
</html>
```